Flyer in Creole

Instructions for Designer
Objective: Create two versions of the flyer for Bricamel dental services: one in French and one in Creole. Target audience is elders of the haitian community in Montreal so include picture of an older person with a darker skin complexion.

I have included our original flyer.

Bricamel - Sèvis Dantè pou Granmoun Aje
Nou ofri swen dantè san frè pou moun 65 an e plis!

La Clinique Dentaire Bricamel gen kè kontan patisipe nan Pwogram Dantè Solèvan (PDSV). Si w gen 65 an oubyen plis, ou ka resevwa swen dantè gratis, san frè siplemantè si w kalifye.

Kijan pou Kalifye?

Si w gen 65 an ou plis, ou ka jwenn tretman dantè san frè.
Vizite: https://www.swendanteprogram.example/aplike/dantè.html pou w aplike epi w konnen si w kalifye.
Sèvis Nou Ofri:

Netwayaj dantè: Sante bouch ou enpòtan, fè yon netwayaj pwofesyonèl pou prezève sante dantè w.
Egzamen ak radyografi: Pran yon randevou pou yon egzamen konplè ak radyografi.
Ekstraksyon dantè: Retire dan ki domaje oswa ki fè w mal.
Ijans dantè: Tretman rapid pou doulè, dan kase, oswa lòt ijans.
Pwotèz dantè konplè ak pasyèl: Nou ranplase dan ki manke yo pou yon bèl souri ak bon sante.
Rele Kounye a pou Fiks yon Randevou: 514-782-4695
Klinik Bricamel - 2863 Rue Marcoux-Belval E, 2yèm etaj, Montreal, QC H2K 3R8
Design Elements:
Use images that resonate with the Creole-speaking community.
Ensure the text is clear and accessible.

```html
<!DOCTYPE html>
<html lang="ht">
<head>
<meta charset="utf-8">
<title>Bricamel – Sèvis Dantè pou Granmoun Aje</title>
<link rel="stylesheet" href="https://fonts.googleapis.com/css2?family=Source+Serif+4:opsz,wght@8..60,400;8..60,600;8..60,700;8..60,800&display=swap">
<style>
  :root {
    --navy: #22324d;
    --navy-text: #243350;
    --sky: #a9c8f0;
    --paper-light: #f7f7f7;
    --paper-edge: #d6d6d6;
    --ink: #1b1b1b;
    --stage: #222222;
    --white: #ffffff;
  }
  * { margin: 0; padding: 0; box-sizing: border-box; }
  html, body { width: 1200px; height: 1200px; overflow: hidden; }
  body {
    background: var(--stage);
    font-family: "Source Serif 4", Georgia, serif;
    color: var(--ink);
  }
  .flyer {
    position: absolute;
    left: 136px; top: 0;
    width: 927px; height: 1200px;
    overflow: hidden;
    background: radial-gradient(ellipse at 50% 55%, var(--paper-light) 0%, #ececec 45%, var(--paper-edge) 100%);
  }
  .flyer-art { position: absolute; left: 0; top: 0; width: 927px; height: 1200px; }
  .logo-name {
    position: absolute;
    left: 65px; top: 360px; width: 292px;
    text-align: center;
    font-size: 62px; font-weight: 400;
    color: var(--navy);
    letter-spacing: -0.5px;
  }
  .headline {
    position: absolute;
    left: 356px; top: 466px; width: 560px;
    font-size: 48px; font-weight: 800;
    line-height: 51px;
    color: var(--navy-text);
    letter-spacing: -0.4px;
  }
  .tagline {
    position: absolute;
    left: 356px; top: 574px; width: 530px;
    font-size: 24px; font-weight: 400; line-height: 31px;
    color: var(--ink);
  }
  .accent { color: var(--navy-text); font-weight: 700; }
  .intro {
    position: absolute;
    left: 61px; top: 645px; width: 820px;
    font-size: 17.5px; line-height: 26px;
  }
  .divider {
    position: absolute; left: 61px; width: 803px;
    border-top: 1.5px dashed var(--navy);
  }
  .divider--top { top: 712px; }
  .divider--bottom { top: 862px; }
  .section-title {
    position: absolute; left: 0; width: 927px;
    text-align: center;
    font-size: 23px; font-weight: 600;
    color: var(--navy-text);
  }
  .qualify-title { top: 720px; }
  .qualify-text {
    position: absolute; left: 0; width: 927px; text-align: center;
    font-size: 18.5px; font-weight: 700;
  }
  .qualify-lead { top: 754px; }
  .qualify-tail { top: 819px; }
  .apply-link {
    position: absolute;
    left: 61px; top: 781px; width: 806px; height: 36px;
    background: var(--sky);
    border-radius: 3px;
    text-align: center;
    font-size: 18.5px; font-weight: 700; line-height: 36px;
    color: var(--navy-text);
  }
  .services-title { top: 869px; font-size: 24px; }
  .service-card {
    position: absolute;
    width: 387px; height: 70px;
    background: var(--navy);
    border-radius: 10px;
    color: var(--white);
  }
  .service-card svg { position: absolute; left: 5px; top: 9px; }
  .service-name {
    position: absolute; left: 71px; top: 5px;
    font-size: 18px; font-weight: 600; color: var(--sky);
    letter-spacing: -0.2px;
  }
  .service-desc {
    position: absolute; left: 71px; top: 27px; right: 10px;
    font-size: 14px; line-height: 18px; letter-spacing: -0.2px;
  }
  .col-left { left: 58px; }
  .col-right { left: 481px; }
  .row-1 { top: 913px; }
  .row-2 { top: 997px; }
  .row-3 { top: 1081px; }
  .band {
    position: absolute; left: 0; top: 1173px; width: 927px; height: 27px;
    background: var(--navy);
  }
  .call-box {
    position: absolute;
    left: 482px; top: 1081px; width: 385px; height: 119px;
    background: var(--sky);
    border-radius: 12px 12px 0 0;
    text-align: center;
    color: var(--navy-text);
  }
  .call-label { margin-top: 6px; font-size: 19.5px; font-weight: 400; white-space: nowrap; }
  .call-phone { font-size: 50px; font-weight: 800; line-height: 50px; letter-spacing: -1px; margin-top: 2px; }
  .call-address { font-size: 13px; color: var(--ink); margin-top: 8px; white-space: nowrap; }
</style>
</head>
<body>
<main class="flyer">
  <svg class="flyer-art" viewBox="0 0 927 1200" width="927" height="1200">
    <defs>
      <linearGradient id="photo-tones" x1="0" y1="0" x2="1" y2="0.3">
        <stop offset="0" stop-color="#3d4f1f"/>
        <stop offset="0.45" stop-color="#5b6a2c"/>
        <stop offset="0.7" stop-color="#7a4b33"/>
        <stop offset="1" stop-color="#5a3424"/>
      </linearGradient>
    </defs>
    <ellipse class="photo-frame" role="img" aria-label="Foto yon granmoun fanm ki gen po fonse k ap souri, deyò devan fèy vèt"
      cx="466" cy="75" rx="440" ry="371" fill="url(#photo-tones)" stroke="#22324d" stroke-width="8"/>
    <circle class="logo-badge" cx="211" cy="404" r="146" fill="#ffffff" stroke="#22324d" stroke-width="7"/>
  </svg>

  <div class="logo-name">bricamel</div>

  <h1 class="headline">SÈVIS DANTÈ POU<br>GRANMOUN AJE</h1>
  <p class="tagline">Nou ofri swen dantè san frè <span class="accent">pou moun 65 an e plis!</span></p>

  <p class="intro">La Clinique Dentaire Bricamel gen kè kontan patisipe nan <span class="accent">Pwogram Dantè Solèvan (PDSV)</span>.<br>Si w gen 65 an oubyen plis, ou ka resevwa <span class="accent">swen dantè gratis</span>, san frè siplemantè si w kalifye.</p>

  <div class="divider divider--top"></div>
  <h2 class="section-title qualify-title">Kijan pou Kalifye?</h2>
  <p class="qualify-text qualify-lead">Si w gen 65 an ou plis, ou ka jwenn tretman dantè san frè. Vizite:</p>
  <p class="apply-link">https://www.swendanteprogram.example/aplike/dantè.html</p>
  <p class="qualify-text qualify-tail">pou w aplike epi w konnen si w kalifye.</p>
  <div class="divider divider--bottom"></div>

  <h2 class="section-title services-title">Sèvis Nou Ofri</h2>

  <article class="service-card col-left row-1">
    <svg width="52" height="52" viewBox="0 0 52 52"><circle cx="26" cy="26" r="24" fill="none" stroke="#a9c8f0" stroke-width="1.3" stroke-dasharray="4 3"/><path d="M18 22c0-4 4-5 8-3 4-2 8-1 8 3 0 4-2 6-2 10 0 3-2 4-3 1l-1-4c-1-2-3-2-4 0l-1 4c-1 3-3 2-3-1 0-4-2-6-2-10z" fill="#a9c8f0"/><circle cx="20" cy="13" r="2" fill="#a9c8f0"/><circle cx="26" cy="11" r="1.5" fill="#a9c8f0"/></svg>
    <h3 class="service-name">Netwayaj dantè:</h3>
    <p class="service-desc">Sante bouch ou enpòtan, fè yon netwayaj pwofesyonèl pou prezève sante dantè w.</p>
  </article>

  <article class="service-card col-left row-2">
    <svg width="52" height="52" viewBox="0 0 52 52"><circle cx="26" cy="26" r="24" fill="none" stroke="#a9c8f0" stroke-width="1.3" stroke-dasharray="4 3"/><path d="M16 20c0-5 5-6 10-4 5-2 10-1 10 4 0 5-2 8-2 13 0 4-3 5-4 1l-1-5c-1-3-5-3-6 0l-1 5c-1 4-4 3-4-1 0-5-2-8-2-13z" fill="#a9c8f0"/><circle cx="26" cy="23" r="3" fill="#22324d"/></svg>
    <h3 class="service-name">Egzamen ak radyografi:</h3>
    <p class="service-desc">Pran yon randevou pou yon egzamen konplè ak radyografi.</p>
  </article>

  <article class="service-card col-left row-3">
    <svg width="52" height="52" viewBox="0 0 52 52"><circle cx="26" cy="26" r="24" fill="none" stroke="#a9c8f0" stroke-width="1.3" stroke-dasharray="4 3"/><path d="M19 31c0-3 3-4 7-2 4-2 7-1 7 2 0 3-1 5-1 8 0 2-2 3-3 1l-1-3h-4l-1 3c-1 2-3 1-3-1 0-3-1-5-1-8z" fill="#a9c8f0"/><path d="M20 12l6 12M32 12l-6 12" stroke="#a9c8f0" stroke-width="2.5" stroke-linecap="round"/></svg>
    <h3 class="service-name">Ekstraksyon dantè:</h3>
    <p class="service-desc">Retire dan ki domaje oswa ki fè w mal.</p>
  </article>

  <article class="service-card col-right row-1">
    <svg width="52" height="52" viewBox="0 0 52 52"><circle cx="26" cy="26" r="24" fill="none" stroke="#a9c8f0" stroke-width="1.3" stroke-dasharray="4 3"/><path d="M16 20c0-5 5-6 10-4 5-2 10-1 10 4 0 5-2 8-2 13 0 4-3 5-4 1l-1-5c-1-3-5-3-6 0l-1 5c-1 4-4 3-4-1 0-5-2-8-2-13z" fill="#a9c8f0"/><circle cx="19" cy="18" r="6" fill="#22324d" stroke="#a9c8f0" stroke-width="1.5"/><path d="M19 15v6M16 18h6" stroke="#a9c8f0" stroke-width="1.8"/></svg>
    <h3 class="service-name">Ijans dantè:</h3>
    <p class="service-desc">Tretman rapid pou doulè, dan kase, oswa lòt ijans.</p>
  </article>

  <article class="service-card col-right row-2">
    <svg width="52" height="52" viewBox="0 0 52 52"><circle cx="26" cy="26" r="24" fill="none" stroke="#a9c8f0" stroke-width="1.3" stroke-dasharray="4 3"/><path d="M12 34c0-12 6-18 14-18s14 6 14 18" fill="none" stroke="#a9c8f0" stroke-width="5" stroke-linecap="round"/></svg>
    <h3 class="service-name">Pwotèz dantè konplè ak pasyèl:</h3>
    <p class="service-desc">Nou ranplase dan ki manke yo pou yon bèl souri ak bon sante.</p>
  </article>

  <div class="band"></div>

  <section class="call-box">
    <p class="call-label">Rele Kounye a pou Fiks yon Randevou:</p>
    <p class="call-phone">514-782-4695</p>
    <p class="call-address">2863 Rue Marcoux-Belval E, 2yèm etaj, Montreal, QC H2K 3R8</p>
  </section>
</main>
</body>
</html>
```